Strategic Objective - Internal

Take text supplied in a word document and make a stylish, professional document using elements of our brand .This is an internal document for presentation to our small team . Have attached an example document - please do not copy this - this is just to give you the concept. I would like to be able to edit the text in the document you supply back to me also (In word or photoshop)

Our website is www.toradvent.com.au

Have attached out logo
Thank you

Target Market(s)

Our staff

Industry/Entity Type

Mining, Earthmoving

Requirements
Must have
• Professional, stylish presentation
Nice to have
• Our market includes Australia, Papua New Guinea and teh South Pacific - any graphic that supports this. We are an importer and exporter - any graphics that support this.

```html
<!DOCTYPE html>
<html lang="en">
<head>
<meta charset="utf-8">
<title>Toradvent – Strategic Objectives</title>
<link href="https://fonts.googleapis.com/css2?family=Roboto:wght@300;400;700&display=swap" rel="stylesheet">
<style>
  :root {
    --navy: #2f3578;
    --green: #8cbf55;
    --green-soft: rgba(140, 191, 85, 0.92);
    --ink: #3a3a3a;
    --white: #ffffff;
    --blob: #efefef;
  }
  * { margin: 0; padding: 0; box-sizing: border-box; }
  html, body { width: 900px; height: 1200px; overflow: hidden; background: var(--white); }
  body { font-family: "Roboto", Arial, sans-serif; color: var(--ink); position: relative; }

  .hero {
    position: absolute; left: 0; top: 0; width: 900px; height: 688px;
    background:
      radial-gradient(ellipse 260px 240px at 700px 500px, rgba(120,108,80,0.55), rgba(120,108,80,0) 70%),
      linear-gradient(180deg, #ffffff 0%, #fbfbfa 28%, #e6e6e3 48%, #b9b7b2 64%, #a7a49e 80%, #c9c6c0 100%);
  }

  .brand {
    position: absolute; top: 52px; left: 640px;
    display: flex; align-items: center; gap: 10px;
  }
  .brand-dot { width: 30px; height: 30px; border-radius: 50%; background: var(--green); }
  .brand-name { font-weight: 700; font-size: 28px; color: var(--navy); letter-spacing: 0.5px; }

  .tangibles { position: absolute; left: 85px; top: 100px; }
  .section-title { font-weight: 700; font-size: 33px; color: var(--navy); line-height: 1.2; }
  .tangibles-intro { font-weight: 300; font-size: 19px; margin-top: 8px; color: var(--ink); }
  .turnover { font-weight: 300; font-size: 23px; margin-top: 4px; color: var(--ink); }
  .turnover strong { font-weight: 700; font-size: 30px; color: var(--navy); }

  .stats {
    position: absolute; left: 85px; top: 272px;
    display: grid; grid-template-columns: 166px 166px; grid-auto-rows: 128px;
    column-gap: 26px; row-gap: 26px;
  }
  .stat {
    background: var(--green-soft); color: var(--white);
    display: flex; flex-direction: column; align-items: center; justify-content: center;
    text-align: center; padding: 0 10px;
  }
  .stat-value { font-weight: 700; font-size: 31px; line-height: 1.1; margin-bottom: 6px; }
  .stat-label { font-weight: 400; font-size: 19px; line-height: 1.3; }

  .promise { position: absolute; left: 85px; top: 726px; width: 400px; }
  .promise .section-title { margin-bottom: 20px; }
  .promise p { font-weight: 300; font-size: 19.5px; line-height: 29px; margin-bottom: 12px; }

  .handshake-art {
    position: absolute; left: 535px; top: 858px; width: 318px; height: 242px;
  }
</style>
</head>
<body>
  <div class="hero" role="img" aria-label="Photograph of a large mining haul truck on a dusty quarry road under a pale sky"></div>

  <div class="brand">
    <span class="brand-dot"></span>
    <span class="brand-name">TORADVENT</span>
  </div>

  <section class="tangibles">
    <h1 class="section-title">TANGIBLES</h1>
    <p class="tangibles-intro">In the 2024-2025 Financial year we will have</p>
    <p class="turnover">Annual turnover of <strong>18M</strong></p>
  </section>

  <div class="stats">
    <div class="stat"><span class="stat-value">21%</span><span class="stat-label">Gross profit</span></div>
    <div class="stat"><span class="stat-value">200</span><span class="stat-label">Average Quotes per week</span></div>
    <div class="stat"><span class="stat-value">52%</span><span class="stat-label">Conversion rate</span></div>
    <div class="stat"><span class="stat-value">10%</span><span class="stat-label">Annual growth rate</span></div>
  </div>

  <section class="promise">
    <h2 class="section-title">Our Brand Promise</h2>
    <p>In every interaction with our business our customers know that they are working with the best – they will not find better service or overall value anywhere else – and this gets reinforced by every interaction they have with us.&nbsp; As well as the physical products they are buying peace of mind.</p>
    <p>We define being the best in terms of Knowledge, Responsiveness, Accuracy, Competitive pricing, Consistency and Understanding</p>
  </section>

  <svg class="handshake-art" viewBox="0 0 318 242" role="img" aria-label="Illustration of two businessmen shaking hands">
    <path d="M40 40 C90 0 240 0 290 40 C325 80 320 170 280 215 C230 250 90 250 40 210 C0 170 0 80 40 40 Z" fill="var(--blob)"/>
  </svg>
</body>
</html>
```